BrindleStaffing Business Card Design

We are a staffing company finding positions for dedicated nurses and physicians.

Target Market(s)

Business Professionals

Industry/Entity Type

Staffing

Contact Information for Business Card

Gregory Malden
Chairman
417 39th Crescent South
SAINT PETERSBURG FL 33719
813-555-0147 Mobile
813-555-0183 Fax
gmalden@brindlestaffing.example
www.brindlestaffing.example

Font styles to use
Sans Serif

Colors
fbee3e
f04a50
f37122

Requirements
Must have
• Logo Attached, see colors below. We'd like to see Yellow, Orange and Red.

```html
<!DOCTYPE html>
<html lang="en">
<head>
<meta charset="utf-8">
<title>BrindleStaffing Business Card</title>
<link rel="stylesheet" href="https://fonts.googleapis.com/css2?family=Work+Sans:wght@400;500;600&display=swap">
<style>
  :root {
    --bg: #3a312c;
    --card: #141414;
    --card-edge: #1d1d1d;
    --yellow: #fbee3e;
    --orange: #f37122;
    --red: #f04a50;
    --white: #f2f2f2;
  }
  * { margin: 0; padding: 0; box-sizing: border-box; }
  html, body { width: 1200px; height: 716px; overflow: hidden; }
  body {
    background: var(--bg);
    font-family: "Work Sans", sans-serif;
    display: flex;
    align-items: center;
    justify-content: center;
    gap: 40px;
  }
  .card {
    position: relative;
    width: 540px;
    height: 309px;
    background: linear-gradient(160deg, var(--card-edge), var(--card));
    border-radius: 4px;
    overflow: hidden;
    box-shadow: 0 14px 30px rgba(0,0,0,.45);
  }
  .card-front {
    display: flex;
    align-items: center;
    justify-content: center;
    border-bottom: 5px solid var(--red);
  }
  .brand-name {
    font-weight: 600;
    color: var(--orange);
    letter-spacing: -0.5px;
  }
  .card-front .brand-name { font-size: 46px; }
  .card-back .brand-name {
    position: absolute;
    top: 40px;
    right: 32px;
    font-size: 28px;
  }
  .person {
    position: absolute;
    top: 40px;
    left: 36px;
  }
  .person-name {
    font-size: 22px;
    font-weight: 500;
    letter-spacing: 1px;
    text-transform: uppercase;
  }
  .first-name { color: var(--yellow); }
  .last-name { color: var(--orange); }
  .person-title {
    font-size: 12px;
    color: var(--white);
    margin-top: 2px;
  }
  .divider {
    position: absolute;
    top: 104px;
    left: 36px;
    right: 32px;
    height: 1px;
    background: var(--red);
  }
  .contact-list {
    position: absolute;
    top: 116px;
    left: 36px;
    list-style: none;
    font-size: 12.5px;
    color: var(--white);
    line-height: 1.5;
  }
  .contact-list li { display: flex; align-items: center; gap: 7px; }
  .contact-list svg { width: 10px; height: 10px; flex: none; }
  .label { color: var(--yellow); margin-left: 4px; }
  .accent { color: var(--orange); }
  .address {
    position: absolute;
    top: 126px;
    right: 32px;
    text-align: right;
    font-size: 13px;
    font-style: normal;
    color: var(--white);
    line-height: 1.5;
    letter-spacing: .5px;
  }
  .swoosh {
    position: absolute;
    left: 0;
    bottom: 0;
    width: 540px;
    height: 309px;
  }
</style>
</head>
<body>
  <section class="card card-front" aria-label="Card front">
    <span class="brand-name">BrindleStaffing</span>
  </section>

  <section class="card card-back" aria-label="Card back">
    <svg class="swoosh" viewBox="0 0 540 309" aria-hidden="true">
      <path d="M0 232 C130 268 310 294 540 302 L540 309 L0 309 Z" fill="var(--red)"/>
      <path d="M0 216 C120 260 290 292 440 299" fill="none" stroke="var(--yellow)" stroke-width="4" stroke-linecap="round"/>
    </svg>

    <div class="person">
      <div class="person-name"><span class="first-name">Gregory</span> <span class="last-name">Malden</span></div>
      <div class="person-title">Chairman</div>
    </div>

    <span class="brand-name">BrindleStaffing</span>

    <div class="divider"></div>

    <ul class="contact-list">
      <li>
        <svg viewBox="0 0 10 10"><path d="M2 1 L4 1 L4.5 3 L3.3 3.8 Q4.5 6 6.2 6.7 L7 5.5 L9 6 L9 8 Q5 9 2 5 Q1 3 2 1 Z" fill="var(--yellow)"/></svg>
        <span>813-555-0147<span class="label">Mobile</span></span>
      </li>
      <li>
        <svg viewBox="0 0 10 10"><rect x="2.5" y="1" width="5" height="3" fill="none" stroke="var(--yellow)"/><rect x="1" y="4" width="8" height="4.5" fill="var(--yellow)"/></svg>
        <span>813-555-0183<span class="label">Fax</span></span>
      </li>
      <li>
        <svg viewBox="0 0 10 10"><rect x="1" y="2.5" width="8" height="5.5" fill="none" stroke="var(--yellow)"/><path d="M1 2.5 L5 5.5 L9 2.5" fill="none" stroke="var(--yellow)"/></svg>
        gmalden@brindlestaffing.example
      </li>
      <li>
        <svg viewBox="0 0 10 10"><circle cx="5" cy="5" r="4" fill="none" stroke="var(--yellow)"/><path d="M1 5 H9 M5 1 Q2.5 5 5 9 M5 1 Q7.5 5 5 9" fill="none" stroke="var(--yellow)" stroke-width=".8"/></svg>
        <span>www.<span class="accent">brindlestaffing</span>.example</span>
      </li>
    </ul>

    <address class="address">
      417 39th Crescent South<br>
      SAINT PETERSBURG FL 33719
    </address>
  </section>
</body>
</html>
```